Salt Water Delivery Company Business Card Design

We are a company that delivers natural saltwater (from the ocean) to aquarium companies, restaurants and home marine tanks. I would like a new business card to suit.

Must include Name, company name, abn, contact number and website as well as logo (see attached).

Looking for a design that stands out, has a clean but unique appearance.

Double and single sided entries welcome

Industry/Entity Type

Business

Requirements
Must have
• Logo

```html
<!DOCTYPE html>
<html lang="en">
<head>
<meta charset="utf-8">
<title>Tide Filled – Business Card</title>
<link rel="stylesheet" href="https://fonts.googleapis.com/css2?family=Cabin:wght@500;600&family=Libre+Baskerville&display=swap">
<style>
  :root {
    --bg: #eef0f3;
    --royal: #1f66ea;
    --royal-deep: #1a4fb4;
    --navy: #0e1f6e;
    --teal: #5f9aa0;
    --ink: #0b0b0b;
    --white: #ffffff;
    --mist: #eef4ff;
    --sky: #9bbcf6;
    --serif: "Libre Baskerville", "Book Antiqua", serif;
    --sans: "Cabin", "Helvetica Neue", sans-serif;
  }
  html, body { margin: 0; padding: 0; overflow: hidden; background: var(--bg); }
  .canvas { position: relative; width: 922px; height: 1200px; overflow: hidden; background: var(--bg); }

  .card { position: absolute; width: 703px; height: 467px; border-radius: 12px; overflow: hidden; }
  .card svg.wave { position: absolute; left: 0; top: 0; width: 703px; height: 467px; }

  /* Front */
  .card-front { left: 162px; top: 37px; background: var(--royal); }
  .brand-tile {
    position: absolute; left: 63px; top: 64px; width: 165px; height: 118px;
    background: linear-gradient(160deg, #3a80f2, var(--royal) 55%, #1857d0);
    box-shadow: inset 2px 2px 0 rgba(255,255,255,.35), inset -2px -2px 0 rgba(0,0,0,.25);
    display: flex; align-items: center; justify-content: center;
  }
  .brand-name { font-family: var(--serif); font-size: 22px; color: var(--white); }
  .company-tag {
    position: absolute; left: 412px; top: 239px; width: 300px; height: 45px;
    background: var(--ink); border-radius: 10px 0 0 10px;
    font-family: var(--serif); color: var(--white); font-size: 31px; line-height: 45px;
    padding-left: 28px; box-sizing: border-box; letter-spacing: .5px;
  }
  .contact-name { position: absolute; left: 440px; top: 322px; font-family: var(--sans); font-weight: 500; font-size: 28px; color: var(--white); }
  .contact-phone { position: absolute; left: 440px; top: 358px; font-family: var(--sans); font-weight: 600; font-size: 19px; color: var(--white); }
  .web-band {
    position: absolute; left: 0; top: 435px; width: 703px; height: 32px;
    background: var(--ink); border-radius: 12px 0 0 0;
    font-family: var(--serif); color: var(--white); font-size: 22px; line-height: 34px;
    text-align: center; letter-spacing: .3px;
  }

  /* Back */
  .card-back {
    left: 168px; top: 542px;
    background: linear-gradient(125deg, var(--white) 0%, var(--mist) 22%, var(--sky) 42%, var(--mist) 55%, #c7d9fb 75%, var(--sky) 100%);
  }
  .back-title { position: absolute; left: 0; width: 758px; top: 180px; text-align: center; font-family: var(--serif); font-size: 34px; color: var(--ink); line-height: 1; }
  .back-sub { position: absolute; left: 0; width: 758px; top: 213px; text-align: center; font-family: var(--serif); font-size: 20px; color: var(--ink); line-height: 1; }
  .back-details { position: absolute; left: 374px; top: 283px; font-family: var(--serif); font-size: 15.5px; line-height: 24px; color: var(--ink); margin: 0; padding: 0; list-style: none; white-space: nowrap; }
</style>
</head>
<body>
<div class="canvas">

  <section class="card card-front">
    <svg class="wave" viewBox="0 0 703 467" aria-hidden="true">
      <path d="M0 0 H703 V126 C600 100 470 95 330 60 C270 40 230 10 180 18 C110 28 40 60 0 80 Z" fill="var(--royal-deep)"/>
      <path d="M0 80 C40 60 110 28 180 18 C230 10 270 40 330 60 C470 95 600 100 703 126" fill="none" stroke="var(--teal)" stroke-width="7"/>
      <path d="M0 88 C40 68 110 36 180 26 C230 18 270 48 330 68 C470 103 600 108 703 134" fill="none" stroke="var(--navy)" stroke-width="6"/>
    </svg>
    <div class="brand-tile"><span class="brand-name">Tide Filled</span></div>
    <div class="company-tag">TIDE FILLED</div>
    <div class="contact-name">Reid Marlow</div>
    <div class="contact-phone">P-0491570156</div>
    <div class="web-band">www.seawaterhaulage.com.au</div>
  </section>

  <section class="card card-back">
    <svg class="wave" viewBox="0 0 703 467" aria-hidden="true">
      <path d="M0 400 C60 430 120 452 190 448 C300 440 430 400 560 385 C620 378 670 372 703 362 V467 H0 Z" fill="var(--royal-deep)"/>
      <path d="M0 400 C60 430 120 452 190 448 C300 440 430 400 560 385 C620 378 670 372 703 362" fill="none" stroke="var(--teal)" stroke-width="7"/>
      <path d="M0 410 C60 440 120 462 190 458 C300 450 430 410 560 395 C620 388 670 382 703 372" fill="none" stroke="var(--navy)" stroke-width="6"/>
    </svg>
    <div class="back-title">TIDE FILLED</div>
    <div class="back-sub">Seawater Haulage</div>
    <ul class="back-details">
      <li>Web:www.seawaterhaulage.com.au</li>
      <li>E-mail:info@seawaterhaulage.com.au</li>
      <li>ABN:12 345 678 901</li>
    </ul>
  </section>

</div>
</body>
</html>
```